Business Card for a Wedding Films Business

We require a business card design for our business 'Lewis Marrow Wedding Films'. The logo needs to look classy and high end.

Target Market(s)

Wedding Couples

Contact Information for Business Card

Lewis Marrow Wedding Films
07312 605 227
films@lewismarrowreels.com
www.lewismarrowreels.com

Facebook: @lewismarrowweddingfilms
Instagram: @lewismarrowfilms

Font styles to use
Sans Serif

Requirements
Must have
• Social media icons - Facebook and Instagram

```html
<!DOCTYPE html>
<html lang="en">
<head>
<meta charset="utf-8">
<title>Lewis Marrow Wedding Films – Business Card</title>
<link href="https://fonts.googleapis.com/css2?family=Open+Sans:wght@400;600&display=swap" rel="stylesheet">
<style>
  :root {
    --backdrop: #dcdcda;
    --card-white: #ffffff;
    --card-black: #252525;
    --ink: #111111;
    --ink-soft: #3a3a3a;
    --rule: #444444;
    --emboss: #1b1b1b;
  }
  * { margin: 0; padding: 0; box-sizing: border-box; }
  html, body {
    width: 1200px; height: 801px; overflow: hidden;
    background: var(--backdrop);
    font-family: "Open Sans", sans-serif;
  }
  .stage {
    position: relative; width: 1200px; height: 801px;
    display: flex; align-items: center; justify-content: center; gap: 60px;
  }
  .card {
    width: 520px; height: 300px; position: relative;
    box-shadow: 0 6px 18px rgba(0,0,0,0.18);
  }
  .card--front { background: var(--card-white); display: flex; align-items: center; }
  .card--back { background: var(--card-black); display: flex; align-items: center; justify-content: center; }

  .wordmark {
    font-family: "Open Sans", sans-serif;
    font-weight: 600;
    text-transform: uppercase;
    text-align: center;
    letter-spacing: 0.22em;
    line-height: 1.5;
  }
  .card--front .wordmark {
    color: var(--ink); font-size: 15px;
    width: 230px; padding-left: 22px;
  }
  .card--back .wordmark { color: var(--emboss); font-size: 22px; }

  .divider {
    width: 1px; height: 110px; background: var(--rule); margin: 0 18px 0 10px;
  }
  .contact-list { list-style: none; }
  .contact-item {
    display: flex; align-items: center; gap: 8px;
    color: var(--ink-soft); font-size: 13.5px; line-height: 22px;
  }
  .contact-icon { width: 11px; height: 11px; flex: none; }
</style>
</head>
<body>
<main class="stage">
  <section class="card card--front" aria-label="Business card front">
    <p class="wordmark">Lewis Marrow<br>Wedding Films</p>
    <span class="divider"></span>
    <ul class="contact-list">
      <li class="contact-item">
        <svg class="contact-icon" viewBox="0 0 12 12" aria-hidden="true"><path d="M2.5 1 4.5 1 5.5 3.8 4.2 4.8C4.9 6.3 5.7 7.1 7.2 7.8L8.2 6.5 11 7.5 11 9.5C11 10.3 10.3 11 9.5 11 5 11 1 7 1 2.5 1 1.7 1.7 1 2.5 1Z" fill="#222"/></svg>
        07312 605 227
      </li>
      <li class="contact-item">
        <svg class="contact-icon" viewBox="0 0 12 12" aria-hidden="true"><rect x="0.5" y="2.5" width="11" height="7.5" fill="#222"/><path d="M0.8 2.8 6 7 11.2 2.8" stroke="#fff" stroke-width="1" fill="none"/></svg>
        films@lewismarrowreels.com
      </li>
      <li class="contact-item">
        <svg class="contact-icon" viewBox="0 0 12 12" aria-hidden="true"><circle cx="6" cy="6" r="5" fill="none" stroke="#222" stroke-width="1.3"/><ellipse cx="6" cy="6" rx="2" ry="5" fill="none" stroke="#222" stroke-width="1"/><path d="M1 6H11" stroke="#222" stroke-width="1"/></svg>
        www.lewismarrowreels.com
      </li>
      <li class="contact-item">
        <svg class="contact-icon" viewBox="0 0 12 12" aria-hidden="true"><rect x="1" y="1" width="10" height="10" fill="#222"/></svg>
        @lewismarrowweddingfilms
      </li>
      <li class="contact-item">
        <svg class="contact-icon" viewBox="0 0 12 12" aria-hidden="true"><rect x="1.5" y="1.5" width="9" height="9" fill="none" stroke="#222" stroke-width="1.3"/></svg>
        @lewismarrowfilms
      </li>
    </ul>
  </section>

  <section class="card card--back" aria-label="Business card back">
    <p class="wordmark">Lewis Marrow<br>Wedding Films</p>
  </section>
</main>
</body>
</html>
```